2 Creative Website Banners for Furniture Brand

Morning Davoskel....
The get a great night sleep banner is complete - we are happy with that one.
Ive uploaded a slightly different concept for the other banner below. This is just something rough ive thrown together. But you can see I have added a curve, a maroon coloured background which is slightly transparent and a big heart in the background....
I do not necessarily want to use this heart image but something a bit like this (a nice graphic, gif etc) but something quite elegant faded in, or perhaps a number of hearts (done in a tasteful way). Also can we keep the typography in the same format as you can see for this one.
Nearly there :)!
Industry/Entity Type
Furniture

```html
<!DOCTYPE html>
<html lang="en">
<head>
<meta charset="utf-8">
<title>Find a Look You Love – Bedrooms Banner</title>
<link rel="stylesheet" href="https://fonts.googleapis.com/css2?family=Crimson+Text:wght@400;600&family=Raleway:wght@500;700&display=swap">
<style>
  :root {
    --plum-deep: #3a1d3b;
    --plum: #4a2a4b;
    --plum-soft: #5a3a5a;
    --room-light: #8c8590;
    --room-mid: #6a6270;
    --room-dark: #3a3540;
    --gold: #c49b68;
    --gold-button: #c9a06c;
    --ink-button: #3d1f3e;
    --text-light: #ffffff;
  }
  * { margin: 0; padding: 0; box-sizing: border-box; }
  html, body {
    width: 1200px;
    height: 356px;
    overflow: hidden;
    background: var(--plum-deep);
  }
  .banner {
    position: relative;
    width: 1200px;
    height: 356px;
    overflow: hidden;
  }
  .banner__art {
    position: absolute;
    inset: 0;
    width: 1200px;
    height: 356px;
    display: block;
  }
  .banner__copy {
    position: absolute;
    left: 194px;
    top: 64px;
    width: 270px;
    color: var(--text-light);
  }
  .banner__kicker {
    font-family: "Raleway", sans-serif;
    font-weight: 500;
    font-size: 21px;
    letter-spacing: 4.2px;
    line-height: 1;
    white-space: nowrap;
  }
  .banner__headline {
    font-family: "Crimson Text", serif;
    font-weight: 400;
    font-size: 60px;
    letter-spacing: 21px;
    line-height: 1;
    margin-top: 16px;
    white-space: nowrap;
  }
  .banner__lede {
    font-family: "Crimson Text", serif;
    font-size: 15.5px;
    line-height: 19px;
    text-align: center;
    margin-top: 16px;
    width: 264px;
  }
  .banner__cta {
    position: absolute;
    left: 231px;
    top: 260px;
    width: 187px;
    height: 32px;
    border-radius: 16px;
    background: var(--gold-button);
    color: var(--ink-button);
    font-family: "Raleway", sans-serif;
    font-weight: 700;
    font-size: 13px;
    letter-spacing: 1.6px;
    display: flex;
    align-items: center;
    justify-content: center;
    text-decoration: none;
  }
</style>
</head>
<body>
  <section class="banner">
    <svg class="banner__art" viewBox="0 0 1200 356" xmlns="http://www.w3.org/2000/svg">
      <defs>
        <linearGradient id="room-tones" x1="0" y1="0" x2="1" y2="1">
          <stop offset="0" stop-color="var(--room-dark)"/>
          <stop offset="0.45" stop-color="var(--room-light)"/>
          <stop offset="1" stop-color="var(--room-mid)"/>
        </linearGradient>
        <linearGradient id="plum-tones" x1="0" y1="0" x2="1" y2="0">
          <stop offset="0" stop-color="var(--plum-deep)"/>
          <stop offset="0.6" stop-color="var(--plum)"/>
          <stop offset="1" stop-color="var(--plum-soft)"/>
        </linearGradient>
      </defs>
      <g role="img" aria-label="Photo of a bedroom with an upholstered bed, grey bedding, mirrored bedside tables and a table lamp">
        <rect class="room-photo" x="0" y="0" width="1200" height="356" fill="url(#room-tones)"/>
      </g>
      <g role="img" aria-label="Photo of a mirrored dressing table and stool under a plum tint">
        <polygon class="dresser-photo" points="0,0 725,0 558,178 702,356 0,356" fill="url(#plum-tones)"/>
      </g>
      <polyline class="chevron-rule" points="725,0 558,178 702,356" fill="none" stroke="var(--gold)" stroke-width="3"/>
    </svg>

    <div class="banner__copy">
      <p class="banner__kicker">FIND A LOOK YOU</p>
      <h1 class="banner__headline">LOVE</h1>
      <p class="banner__lede">Lorem ipsum not sure what the rest of this will say at the moment</p>
    </div>
    <a class="banner__cta" href="#">SHOPE BEDROOMS</a>
  </section>
</body>
</html>
```